KTRL Business Card Design

Business card for sole operator professional civil and traffic engineer.
Clients are developers and planners who require assistance with traffic strategic master planning advice and design development for access and infrastructure associated with the development.
Colours already in use are greens for the business name and black for other legend. The attached file shows the letterhead template which is currently in use.
Target Market(s)
Professional Clients in development industry
Most clients known to the Principal and card is mostly required to allow ongoing contact
Industry/Entity Type
Business
Contact Information for Business Card
DONALD PLUMWEATHER ADVISORY SERVICES
ABN 37 806 519 174
PO Box 718 KELVALE NSW 2461
Donald Plumweather 0413 885 190
donald.plumweather@farvenmail.com

```html
<!DOCTYPE html>
<html lang="en">
<head>
<meta charset="utf-8">
<title>KTRL Business Card</title>
<link href="https://fonts.googleapis.com/css2?family=Cinzel:wght@500&family=Michroma&family=Open+Sans:wght@400;600&display=swap" rel="stylesheet">
<style>
  :root {
    --backdrop: #cfcfcf;
    --card-dark: #141414;
    --card-dark-edge: #262626;
    --card-light: #ffffff;
    --green: #1fae45;
    --green-bright: #35c85a;
    --ink: #1a1a1a;
    --white: #f2f2f2;
    --faint: #eef2ee;
  }
  * { margin: 0; padding: 0; box-sizing: border-box; }
  html, body { width: 1200px; height: 900px; overflow: hidden; }
  body {
    background: var(--backdrop);
    font-family: "Open Sans", sans-serif;
    position: relative;
  }
  .card {
    position: absolute;
    top: 300px;
    width: 525px;
    height: 300px;
    border-radius: 22px;
    overflow: hidden;
    box-shadow: 0 14px 30px rgba(0,0,0,0.22);
  }

  /* Front */
  .card-front {
    left: 50px;
    background: radial-gradient(ellipse at 50% 40%, var(--card-dark-edge), var(--card-dark) 75%);
    display: flex;
    flex-direction: column;
    align-items: center;
    justify-content: center;
    color: var(--white);
  }
  .brand-mark {
    display: flex;
    align-items: center;
    gap: 12px;
  }
  .brand-square {
    width: 44px; height: 44px;
    border-radius: 9px;
    background: var(--green);
  }
  .brand-name {
    font-family: "Open Sans", sans-serif;
    font-weight: 600;
    font-size: 34px;
    color: var(--green);
    letter-spacing: 2px;
  }
  .card-front .brand-mark { margin-bottom: 26px; }
  .business-name {
    font-family: "Cinzel", serif;
    font-weight: 500;
    color: var(--green-bright);
    font-size: 27px;
    letter-spacing: 0.5px;
    line-height: 1;
  }
  .business-tagline {
    font-family: "Michroma", sans-serif;
    font-size: 12.5px;
    letter-spacing: 6px;
    margin-top: 9px;
  }

  /* Back */
  .card-back {
    left: 625px;
    background: var(--card-light);
    color: var(--ink);
  }
  .card-back .header {
    position: absolute;
    top: 22px; left: 22px;
    display: flex;
    align-items: center;
    gap: 14px;
  }
  .card-back .brand-square { width: 40px; height: 40px; }
  .card-back .brand-name { font-size: 26px; }
  .card-back .titles { margin-left: 4px; }
  .card-back .business-name { font-size: 20px; }
  .card-back .business-tagline { font-size: 9px; letter-spacing: 4px; margin-top: 6px; color: var(--ink); }
  .watermark-square {
    position: absolute;
    right: -30px; top: 118px;
    width: 140px; height: 140px;
    border-radius: 22px;
    background: var(--faint);
  }
  .person {
    position: absolute;
    top: 138px; left: 26px;
  }
  .person-name {
    font-weight: 600;
    font-size: 17px;
    color: var(--green);
  }
  .person-role { font-size: 10.5px; margin-top: 1px; }
  .contacts {
    position: absolute;
    top: 208px; left: 26px;
    list-style: none;
    font-size: 13px;
    line-height: 17px;
  }
  .contacts li { display: flex; align-items: center; gap: 6px; }
  .contacts svg { width: 14px; height: 14px; fill: var(--green); flex: none; }
  .contacts .no-icon { padding-left: 20px; }
  .footer-band {
    position: absolute;
    left: 0; bottom: 0;
    width: 100%; height: 60px;
  }
</style>
</head>
<body>

  <section class="card card-front">
    <div class="brand-mark">
      <span class="brand-square"></span>
      <span class="brand-name">KTRL</span>
    </div>
    <div class="business-name">DONALD PLUMWEATHER</div>
    <div class="business-tagline">ADVISORY SERVICES</div>
  </section>

  <section class="card card-back">
    <div class="watermark-square"></div>
    <div class="header">
      <div class="brand-mark">
        <span class="brand-square"></span>
        <span class="brand-name">KTRL</span>
      </div>
      <div class="titles">
        <div class="business-name">DONALD PLUMWEATHER</div>
        <div class="business-tagline">ADVISORY SERVICES</div>
      </div>
    </div>

    <div class="person">
      <div class="person-name">Donald Plumweather</div>
      <div class="person-role">Managing Director</div>
    </div>

    <ul class="contacts">
      <li>
        <svg viewBox="0 0 24 24"><path d="M6.6 10.8a15.5 15.5 0 0 0 6.6 6.6l2.2-2.2a1 1 0 0 1 1-.25 11.4 11.4 0 0 0 3.6.57 1 1 0 0 1 1 1V20a1 1 0 0 1-1 1A17 17 0 0 1 3 4a1 1 0 0 1 1-1h3.5a1 1 0 0 1 1 1c0 1.25.2 2.45.57 3.57a1 1 0 0 1-.25 1z"/></svg>
        0413 885 190
      </li>
      <li>
        <svg viewBox="0 0 24 24"><path d="M12 3 2 12h3v8h5v-5h4v5h5v-8h3z"/></svg>
        PO Box 718 KELVALE NSW 2461
      </li>
      <li>
        <svg viewBox="0 0 24 24"><path d="M3 6h18v12H3z" fill="none"/><path d="M3 5h18a1 1 0 0 1 1 1v12a1 1 0 0 1-1 1H3a1 1 0 0 1-1-1V6a1 1 0 0 1 1-1zm9 7.5L20.5 7h-17z"/></svg>
        donald.plumweather@farvenmail.com
      </li>
      <li class="no-icon">ABN 37 806 519 174</li>
    </ul>

    <svg class="footer-band" viewBox="0 0 525 60" preserveAspectRatio="none">
      <path d="M0 44 Q260 30 525 6 L525 60 L0 60 Z" fill="var(--green)"/>
      <path d="M0 48 Q260 36 525 14 L525 60 L0 60 Z" fill="var(--card-dark)"/>
    </svg>
  </section>

</body>
</html>
```